Velsori Biotechnology needs a professional powerpoint design

We would like to re-design our powerpoint template(as attachment 1), it should be based on our current logo (as attachment 2). We hope the new powerpoint template could be more professional and like a biotechnology company with advanced technology.
Velsori Biotechnology is a contract development and manufacturing organization to provide high quality services to our clients in development, lead-in advanced technology and cGMP manufacturing of biopharmaceuticals from clinical to commercial manufacturing. We offers the advanced technology and services to become the best partner for clients from clinical to commercial manufacturing.
Reason: We would like to extend the deadline for this project so that designers can have more time to prepare, thanks.
Target Market(s)
Velsori Biotechnology is a contract development and manufacturing organization to provide high quality services to our clients in development, lead-in advanced technology and cGMP manufacturing of biopharmaceuticals from clinical to commercial manufacturing.
Velsori primary focus on development and manufacturing of glycoprotein pharmaceuticals against breast cancer, supplies KEP Taiwan with KEP-437 & KEP-438 for global clinical trials and commercialization in the future. Velsori offers the advanced technology and services to become the best partner for clients from clinical to commercial manufacturing.
Industry/Entity Type
Biotechnology
Requirements
Must have
- The new powerpoint design should based on our current logo.
Should not have
- The similar design with current powerpoint style. Please don't refer the design style of our current website http://www.velsori-example.com.tw/ as well, we will re-design it soon.

```html
<!DOCTYPE html>
<html lang="en">
<head>
<meta charset="utf-8">
<title>Velsori Biotechnology – Presentation Template</title>
<link href="https://fonts.googleapis.com/css2?family=Ubuntu:wght@400;500;700&display=swap" rel="stylesheet">
<style>
  :root{
    --olive:#8a8c18;
    --leaf:#6f8f2e;
    --leaf-dark:#5d7a24;
    --lime:#b9b52a;
    --orange:#f5a31e;
    --sun:#f7c51e;
    --red:#e53b2c;
    --ink:#3b3b3b;
    --grey:#a9a9a9;
    --white:#ffffff;
  }
  *{box-sizing:border-box;margin:0;padding:0}
  html,body{width:1200px;height:1113px;overflow:hidden;background:#fff;font-family:"Ubuntu",sans-serif;color:var(--ink)}
  .deck{position:relative;width:1200px;height:1113px}
  .slide{position:absolute;width:384px;height:216px;background:var(--white);overflow:hidden;box-shadow:0 1px 4px rgba(0,0,0,.25)}
  .c1{left:8px}.c2{left:408px}.c3{left:808px}
  .r1{top:2px}.r2{top:225px}.r3{top:447px}.r4{top:669px}.r5{top:891px}
  .abs{position:absolute}
  .foot{position:absolute;left:0;right:0;bottom:0;height:7px;background:linear-gradient(90deg,var(--sun),var(--orange))}
  .pg{position:absolute;right:0;bottom:0;width:11px;height:7px;background:var(--leaf);color:#fff;font-size:4px;line-height:7px;text-align:center}
  .brand{position:absolute;display:flex;align-items:center;gap:3px;font-size:10px;font-weight:700;color:var(--ink);letter-spacing:.3px}
  .brand::before{content:"";width:7px;height:7px;border-radius:50%;background:var(--orange)}
  .brand.light{color:#fff}
  .title{position:absolute;font-size:15px;color:var(--olive);font-weight:400;white-space:nowrap}
  .title::after{content:"";display:block;width:34px;height:2px;background:var(--orange);margin-top:4px}
  .title.plain::after{display:none}
  .tiny{font-size:4px;line-height:1.45;color:var(--grey)}
  .tiny.w{color:rgba(255,255,255,.85)}
  .head{font-size:7px;color:var(--olive)}
  .ih{display:block;font-size:6px;font-weight:500;color:var(--olive);margin-bottom:1px}
  .ih.w{color:#fff}
  .item{position:absolute;display:flex;gap:5px;align-items:flex-start}
  .dot{flex:none;width:12px;height:12px;border-radius:50%;background:var(--orange);display:flex;align-items:center;justify-content:center}
  .dot svg{width:8px;height:8px}
  .dot.green{background:var(--leaf)}.dot.red{background:var(--red)}
  .dot.ring{background:none;border:1px solid rgba(255,255,255,.8);width:20px;height:20px}
  .dot.ring svg{width:10px;height:10px}
  .dot.bare{background:none;width:12px}
  .photo{position:absolute}
  .snow-grass{background:linear-gradient(180deg,#f4f6f2 0%,#b9cf8a 45%,#6d9a3a 65%,#e9edf0 100%)}
  .lab{background:linear-gradient(160deg,#f4f5f7,#dfe4ea 60%,#c7d6e8)}
  .tubes{background:linear-gradient(180deg,#e9ecef,#cfd8e1 70%,#7fb3e2)}
  .soil{background:linear-gradient(160deg,#eeeeee 0%,#d8d3cf 45%,#5b4638 70%,#e4e2e0 100%)}
  .teal{background:linear-gradient(140deg,#2f8f95,#46b4b8 50%,#1f6f7b)}
  .sprout{background:linear-gradient(160deg,#e9e6e2,#c7b9a8 50%,#3f3125 75%,#7aa040)}
  .wash-nuts{background:linear-gradient(135deg,#c4b83a 0%,#a8ac38 50%,#8f9a34 100%)}
  .wash-olive{background:linear-gradient(160deg,#8a9a2a 0%,#6f8a2a 55%,#5c7722 100%)}
  .wash-beans{background:linear-gradient(150deg,#cfc23e 0%,#b7b53c 45%,#8fa234 100%)}
  .panel{position:absolute;background:linear-gradient(135deg,#c3b42c,#7f9a2a)}
  .numbox{position:absolute;display:flex;align-items:center;gap:6px;padding-left:6px;color:#fff;height:29px;width:168px}
  .numbox b{font-size:16px;font-weight:500;border-right:1px solid #fff;padding-right:6px;line-height:18px}
  .numbox p{font-size:4px;line-height:1.4}
</style>
</head>
<body>
<svg width="0" height="0" style="position:absolute">
  <defs>
    <symbol id="i-search" viewBox="0 0 10 10"><circle cx="4.2" cy="4.2" r="2.5" fill="none" stroke="#fff" stroke-width="1.3"/><line x1="6" y1="6" x2="8.6" y2="8.6" stroke="#fff" stroke-width="1.5"/></symbol>
    <symbol id="i-pen" viewBox="0 0 10 10"><line x1="2" y1="8" x2="8" y2="2" stroke="#fff" stroke-width="1.8"/></symbol>
    <symbol id="i-chart" viewBox="0 0 10 10"><rect x="1.5" y="6" width="1.6" height="2.5" fill="#fff"/><rect x="4.2" y="4" width="1.6" height="4.5" fill="#fff"/><rect x="6.9" y="2" width="1.6" height="6.5" fill="#fff"/></symbol>
    <symbol id="i-gear" viewBox="0 0 10 10"><circle cx="5" cy="5" r="3.3" fill="none" stroke="#fff" stroke-width="1.6" stroke-dasharray="1.3 1"/><circle cx="5" cy="5" r="1.2" fill="#fff"/></symbol>
    <symbol id="i-bolt" viewBox="0 0 10 10"><path d="M6 1 2.5 5.5H5L4 9 7.5 4.5H5z" fill="#fff"/></symbol>
    <symbol id="i-star" viewBox="0 0 10 10"><path d="M5 1.2 6.1 3.8 8.8 4 6.7 5.8 7.4 8.6 5 7.1 2.6 8.6 3.3 5.8 1.2 4 3.9 3.8z" fill="#fff"/></symbol>
  </defs>
</svg>

<main class="deck">

  <!-- Row 1 -->
  <section class="slide c1 r1">
    <div class="brand" style="left:12px;top:12px">Velsori Biotech</div>
    <h2 class="title" style="left:17px;top:52px">Your Title Goes Here</h2>
    <div class="item" style="left:50px;top:88px;width:170px"><span class="dot"><svg><use href="#i-chart"/></svg></span><div><span class="ih">Heading One</span><p class="tiny">Lorem ipsum dolor sit amet, consectetur adipiscing elit, sed do eiusmod tempor incididunt ut labore magna aliqua.</p></div></div>
    <div class="item" style="left:50px;top:124px;width:170px"><span class="dot"><svg><use href="#i-bolt"/></svg></span><div><span class="ih">Heading Two</span><p class="tiny">Lorem ipsum dolor sit amet, consectetur adipiscing elit, sed do eiusmod tempor incididunt ut labore magna aliqua.</p></div></div>
    <div class="item" style="left:50px;top:161px;width:170px"><span class="dot"><svg><use href="#i-search"/></svg></span><div><span class="ih">Heading Three</span><p class="tiny">Lorem ipsum dolor sit amet, consectetur adipiscing elit, sed do eiusmod tempor incididunt ut labore magna aliqua.</p></div></div>
    <div class="photo lab" style="left:252px;top:5px;width:128px;height:96px" role="img" aria-label="Scientist in lab coat holding a pipette"></div>
    <div class="photo tubes" style="left:252px;top:104px;width:128px;height:100px" role="img" aria-label="Row of test tubes with blue liquid"></div>
    <div class="foot"></div><span class="pg">16</span>
  </section>

  <section class="slide c2 r1 wash-nuts" role="img" aria-label="Quote slide over a photo of assorted nuts and seeds in green-yellow tones">
    <div class="abs" style="left:174px;top:54px;width:36px;height:36px;border-radius:50%;background:var(--leaf);color:#fff;font-size:24px;font-weight:700;text-align:center;line-height:42px">&ldquo;</div>
    <p class="abs" style="left:0;right:0;top:96px;text-align:center;color:#fff;font-size:10px;line-height:1.55">Coming together is a beginning.<br>Keeping together is progress.<br>Working together is success.</p>
    <p class="abs" style="left:0;right:0;top:160px;text-align:center;color:#fff;font-size:5px">- Hollis Warden -</p>
  </section>

  <section class="slide c3 r1">
    <h2 class="title" style="left:17px;top:20px">Our Differences</h2>
    <div class="brand" style="left:310px;top:14px">Velsori</div>
    <div class="panel" style="left:20px;top:64px;width:333px;height:112px">
      <div class="item" style="left:14px;top:15px;width:180px"><span class="dot green"><svg><use href="#i-bolt"/></svg></span><p class="tiny w">Lorem ipsum dolor sit amet, consectetur adipiscing elit, sed do eiusmod tempor incididunt ut labore.</p></div>
      <div class="item" style="left:14px;top:38px;width:180px"><span class="dot green"><svg><use href="#i-gear"/></svg></span><p class="tiny w">Duis aute irure dolor in reprehenderit in voluptate velit esse cillum dolore.</p></div>
      <div class="item" style="left:14px;top:61px;width:180px"><span class="dot green"><svg><use href="#i-pen"/></svg></span><p class="tiny w">Lorem ipsum dolor sit amet, consectetur adipiscing elit, sed do eiusmod tempor incididunt ut labore.</p></div>
      <div class="item" style="left:14px;top:84px;width:180px"><span class="dot green"><svg><use href="#i-search"/></svg></span><p class="tiny w">Duis aute irure dolor in reprehenderit in voluptate velit esse cillum dolore.</p></div>
      <div class="photo snow-grass" style="left:203px;top:15px;width:106px;height:78px;border:2px solid #fff" role="img" aria-label="Green shoots growing through snow"></div>
    </div>
    <div class="foot"></div><span class="pg">18</span>
  </section>

  <!-- Row 2 -->
  <section class="slide c1 r2">
    <div class="photo snow-grass" style="left:0;top:0;width:229px;height:216px" role="img" aria-label="Green shoots growing through snow"></div>
    <div class="panel" style="left:229px;top:0;width:136px;height:216px">
      <div class="brand light" style="left:24px;top:38px">Velsori</div>
      <span class="dot ring abs" style="left:13px;top:73px"><svg><use href="#i-bolt"/></svg></span>
      <span class="dot ring abs" style="left:56px;top:73px"><svg><use href="#i-search"/></svg></span>
      <span class="dot ring abs" style="left:99px;top:73px"><svg><use href="#i-star"/></svg></span>
      <div class="abs" style="left:14px;top:107px;width:112px;height:1px;background:rgba(255,255,255,.5)"></div>
      <h2 class="abs" style="left:14px;top:118px;color:#fff;font-size:15px;font-weight:400;line-height:1.1">Your Title<br>Goes Here</h2>
      <p class="tiny w abs" style="left:14px;top:155px;width:112px">Lorem ipsum dolor sit amet, consectetur adipiscing elit, sed do eiusmod tempor incididunt ut labore et commodo consequat dolore magna aliqua.</p>
      <div class="abs" style="left:0;right:0;bottom:0;height:18px;background:rgba(80,110,30,.35);color:#fff;font-size:5px;text-align:center;line-height:18px">www.yourwebsite.com</div>
    </div>
  </section>

  <section class="slide c2 r2">
    <h2 class="title" style="left:17px;top:20px">Two Column Description</h2>
    <div class="brand" style="left:318px;top:14px">Velsori</div>
    <p class="abs" style="left:21px;top:70px;font-size:7px;color:#555">We are <span style="color:var(--olive)">Velsori Biotech</span></p>
    <div class="abs" style="left:18px;top:100px;width:175px">
      <p class="tiny">Lorem ipsum dolor sit amet, consectetur adipiscing elit, sed do eiusmod tempor incididunt ut labore et dolore magna aliqua. Ut enim ad minim veniam, quis nostrud exercitation ullamco laboris nisi ut aliquip ex ea commodo consequat.</p>
      <p class="tiny" style="margin-top:6px">Duis aute irure dolor in reprehenderit in voluptate velit esse cillum dolore eu fugiat nulla pariatur. Excepteur sint occaecat cupidatat non proident, sunt in culpa qui officia deserunt mollit anim id est laborum.</p>
    </div>
    <div class="abs" style="left:199px;top:100px;width:1px;height:60px;background:#ddd"></div>
    <div class="abs" style="left:208px;top:100px;width:160px">
      <p class="tiny">Lorem ipsum dolor sit amet, consectetur adipiscing elit, sed do eiusmod tempor incididunt ut labore et dolore magna aliqua. Ut enim ad minim veniam, quis nostrud exercitation ullamco laboris nisi ut aliquip ex ea commodo consequat.</p>
      <p class="tiny" style="margin-top:6px">Duis aute irure dolor in reprehenderit in voluptate velit esse cillum dolore eu fugiat nulla pariatur. Excepteur sint occaecat cupidatat non proident, sunt in culpa qui officia deserunt mollit anim id est laborum.</p>
    </div>
    <div class="foot"></div><span class="pg">20</span>
  </section>

  <section class="slide c3 r2 wash-olive" role="img" aria-label="Coffee break slide over a blurred photo of a coffee cup on a table">
    <div class="brand light" style="left:320px;top:20px">Velsori</div>
    <svg class="abs" style="left:180px;top:72px" width="22" height="20" viewBox="0 0 22 20"><path d="M3 8h12v4a6 6 0 0 1-12 0z" fill="#fff"/><path d="M15 9h2a2.5 2.5 0 0 1 0 5h-2" fill="none" stroke="#fff" stroke-width="1.5"/><path d="M7 6c-1-2 1-3 0-5M11 6c-1-2 1-3 0-5" fill="none" stroke="#fff" stroke-width="1.2"/><rect x="1" y="18" width="16" height="1.5" fill="#fff"/></svg>
    <p class="abs" style="left:0;right:0;top:98px;text-align:center;color:#fff;font-size:12px;font-weight:700">COFFEE BREAK</p>
    <p class="abs" style="left:0;right:0;top:113px;text-align:center;color:#fff;font-size:5px">Back in 15 minutes</p>
  </section>

  <!-- Row 3 -->
  <section class="slide c1 r3">
    <div class="photo soil" style="left:0;top:0;width:192px;height:216px" role="img" aria-label="Cupped hands holding dark soil"></div>
    <div class="abs" style="left:192px;top:0;width:192px;height:216px;background:var(--leaf)">
      <div class="brand light" style="left:124px;top:16px">Velsori</div>
      <h2 class="abs" style="left:16px;top:36px;color:#fff;font-size:9px;font-weight:500;line-height:1.5">We are Tarnel Bio<br>Technology to Treat<br>Pulmonary Hypertension</h2>
      <div class="item" style="left:16px;top:86px;width:165px"><span class="dot bare"><svg><use href="#i-search"/></svg></span><div><span class="ih w">Your Text Here</span><p class="tiny w">Lorem ipsum dolor sit amet, consectetur adipiscing elit, sed do eiusmod.</p></div></div>
      <div class="item" style="left:16px;top:117px;width:165px"><span class="dot bare"><svg><use href="#i-pen"/></svg></span><div><span class="ih w">Your Text Here</span><p class="tiny w">Lorem ipsum dolor sit amet, consectetur adipiscing elit, sed do eiusmod.</p></div></div>
      <div class="item" style="left:16px;top:148px;width:165px"><span class="dot bare"><svg><use href="#i-bolt"/></svg></span><div><span class="ih w">Your Text Here</span><p class="tiny w">Lorem ipsum dolor sit amet, consectetur adipiscing elit, sed do eiusmod.</p></div></div>
      <div class="item" style="left:16px;top:179px;width:165px"><span class="dot bare"><svg><use href="#i-gear"/></svg></span><div><span class="ih w">Your Text Here</span><p class="tiny w">Lorem ipsum dolor sit amet, consectetur adipiscing elit, sed do eiusmod.</p></div></div>
    </div>
  </section>

  <section class="slide c2 r3">
    <h2 class="title" style="left:17px;top:20px">Your Title Goes Here</h2>
    <div class="brand" style="left:318px;top:14px">Velsori</div>
    <span class="head abs" style="left:17px;top:56px">Heading Goes Here</span>
    <p class="tiny abs" style="left:17px;top:65px;width:350px">Lorem ipsum adipiscing elit, sed do eiusmod tempor incididunt ut labore et dolore magna aliqua. Ut enim ad minim veniam, quis nostrud exercitation ullamco laboris nisi ut aliquip ex ea commodo consequat.</p>
    <div class="item" style="left:17px;top:94px;width:165px"><span class="dot green"><svg><use href="#i-chart"/></svg></span><div><span class="ih">Service Number One</span><p class="tiny">Lorem ipsum dolor sit amet, consectetur adipiscing elit, sed do eiusmod tempor incididunt ut labore et dolore magna aliqua.</p></div></div>
    <div class="item" style="left:17px;top:130px;width:165px"><span class="dot"><svg><use href="#i-bolt"/></svg></span><div><span class="ih" style="color:var(--orange)">Service Number Two</span><p class="tiny">Lorem ipsum dolor sit amet, consectetur adipiscing elit, sed do eiusmod tempor incididunt ut labore et dolore magna aliqua.</p></div></div>
    <div class="item" style="left:17px;top:168px;width:165px"><span class="dot red"><svg><use href="#i-search"/></svg></span><div><span class="ih" style="color:var(--red)">Service Number One</span><p class="tiny">Lorem ipsum dolor sit amet, consectetur adipiscing elit, sed do eiusmod tempor incididunt ut labore et dolore magna aliqua.</p></div></div>
    <div class="numbox" style="left:200px;top:94px;background:var(--leaf)"><b>1</b><p>Lorem ipsum dolor sit amet, consectetur adipiscing elit, sed do eiusmod tempor incididunt ut labore et dolore magna aliqua.</p></div>
    <div class="numbox" style="left:200px;top:130px;background:var(--orange)"><b>2</b><p>Lorem ipsum dolor sit amet, consectetur adipiscing elit, sed do eiusmod tempor incididunt ut labore et dolore magna aliqua.</p></div>
    <div class="numbox" style="left:200px;top:166px;background:var(--red)"><b>3</b><p>Lorem ipsum dolor sit amet, consectetur adipiscing elit, sed do eiusmod tempor incididunt ut labore et dolore magna aliqua.</p></div>
    <div class="foot"></div><span class="pg">23</span>
  </section>

  <section class="slide c3 r3">
    <div class="brand" style="left:12px;top:18px">Velsori</div>
    <h2 class="title plain" style="left:17px;top:42px;line-height:1.1">Your Title<br>Goes Here</h2>
    <div class="abs" style="left:17px;top:91px;width:90px">
      <p class="tiny">Lorem ipsum dolor sit amet, consectetur adipiscing elit, sed do eiusmod tempor incididunt ut labore et commodo consequat dolore magna aliqua.</p>
      <p class="tiny" style="margin-top:5px">Duis aute irure dolor in reprehenderit in voluptate velit esse cillum dolore eu fugiat nulla pariatur.</p>
      <p class="tiny" style="margin-top:5px">Ut enim ad minim veniam, quis nostrud exercitation ullamco laboris.</p>
    </div>
    <div class="photo teal" style="left:118px;top:5px;width:134px;height:96px" role="img" aria-label="Hands around a glowing digital data screen"></div>
    <div class="photo teal" style="left:255px;top:5px;width:123px;height:96px" role="img" aria-label="Hands around a glowing digital data screen"></div>
    <div class="photo teal" style="left:118px;top:104px;width:134px;height:93px" role="img" aria-label="Open hands beneath a glowing digital data screen"></div>
    <div class="photo teal" style="left:255px;top:104px;width:123px;height:93px" role="img" aria-label="Open hand beneath a glowing digital data screen"></div>
    <div class="foot"></div><span class="pg">24</span>
  </section>

  <!-- Row 4 -->
  <section class="slide c1 r4">
    <h2 class="title" style="left:17px;top:20px">Four Bullets with Paragraph</h2>
    <div class="brand" style="left:318px;top:14px">Velsori</div>
    <div class="item" style="left:25px;top:70px;width:80px"><span class="dot"><svg><use href="#i-search"/></svg></span><div><span class="ih">Your Text Here</span><p class="tiny">Lorem ipsum dolor sit amet, consectetur adipiscing elit, sed do eiusmod.</p></div></div>
    <div class="item" style="left:110px;top:70px;width:80px"><span class="dot"><svg><use href="#i-pen"/></svg></span><div><span class="ih">Your Text Here</span><p class="tiny">Lorem ipsum dolor sit amet, consectetur adipiscing elit, sed do eiusmod.</p></div></div>
    <div class="item" style="left:25px;top:133px;width:80px"><span class="dot"><svg><use href="#i-gear"/></svg></span><div><span class="ih">Your Text Here</span><p class="tiny">Lorem ipsum dolor sit amet, consectetur adipiscing elit, sed do eiusmod.</p></div></div>
    <div class="item" style="left:110px;top:133px;width:80px"><span class="dot"><svg><use href="#i-bolt"/></svg></span><div><span class="ih">Your Text Here</span><p class="tiny">Lorem ipsum dolor sit amet, consectetur adipiscing elit, sed do eiusmod.</p></div></div>
    <div class="abs" style="left:211px;top:70px;width:160px">
      <span class="head">Heading Goes Here</span>
      <p class="tiny" style="margin-top:5px">Lorem ipsum dolor sit amet, consectetur adipiscing elit, sed do eiusmod tempor incididunt ut labore et commodo consequat dolore magna aliqua.</p>
      <p class="tiny" style="margin-top:5px">Duis aute irure dolor in reprehenderit in voluptate velit esse cillum dolore eu fugiat nulla pariatur.</p>
      <p class="tiny" style="margin-top:5px">Ut enim ad minim veniam, quis nostrud exercitation ullamco laboris nisi ut aliquip ex ea commodo consequat.</p>
    </div>
    <div class="foot"></div><span class="pg">25</span>
  </section>

  <section class="slide c2 r4">
    <h2 class="title" style="left:17px;top:20px">Your Title</h2>
    <div class="brand" style="left:318px;top:14px">Velsori</div>
    <div class="abs" style="left:17px;top:68px;width:100px">
      <span class="head">Heading Goes Here</span>
      <p class="tiny" style="margin-top:4px">Lorem ipsum dolor sit amet, consectetur adipiscing elit, sed do eiusmod tempor incididunt ut labore et commodo consequat dolore magna aliqua.</p>
      <p class="tiny" style="margin-top:5px">Duis aute irure dolor in reprehenderit in voluptate velit esse cillum dolore eu fugiat nulla pariatur.</p>
      <p class="tiny" style="margin-top:5px">Ut enim ad minim veniam, quis nostrud exercitation ullamco laboris nisi ut aliquip ex ea commodo consequat.</p>
    </div>
    <div class="photo snow-grass" style="left:122px;top:38px;width:140px;height:167px" role="img" aria-label="Green shoots growing through snow"></div>
    <div class="item" style="left:273px;top:64px;width:105px"><span class="dot"><svg><use href="#i-search"/></svg></span><div><span class="ih">Your Text Here</span><p class="tiny">Lorem ipsum dolor sit amet, adipiscing elit, sed do eiusmod.</p></div></div>
    <div class="item" style="left:273px;top:95px;width:105px"><span class="dot"><svg><use href="#i-pen"/></svg></span><div><span class="ih">Your Text Here</span><p class="tiny">Lorem ipsum dolor sit amet, adipiscing elit, sed do eiusmod.</p></div></div>
    <div class="item" style="left:273px;top:126px;width:105px"><span class="dot"><svg><use href="#i-bolt"/></svg></span><div><span class="ih">Your Text Here</span><p class="tiny">Lorem ipsum dolor sit amet, adipiscing elit, sed do eiusmod.</p></div></div>
    <div class="item" style="left:273px;top:157px;width:105px"><span class="dot"><svg><use href="#i-gear"/></svg></span><div><span class="ih">Your Text Here</span><p class="tiny">Lorem ipsum dolor sit amet, adipiscing elit, sed do eiusmod.</p></div></div>
    <div class="foot"></div><span class="pg">26</span>
  </section>

  <section class="slide c3 r4">
    <h2 class="title" style="left:17px;top:20px">Text &amp; Bullet Area</h2>
    <div class="brand" style="left:318px;top:14px">Velsori</div>
    <div class="abs" style="left:19px;top:64px;width:100px">
      <span class="head">Heading Goes Here</span>
      <p class="tiny" style="margin-top:5px">Lorem ipsum dolor sit amet, consectetur adipiscing elit, sed do eiusmod tempor incididunt ut labore et commodo consequat dolore magna aliqua.</p>
      <p class="tiny" style="margin-top:5px">Duis aute irure dolor in reprehenderit in voluptate velit esse cillum dolore eu fugiat nulla pariatur.</p>
      <p class="tiny" style="margin-top:5px">Ut enim ad minim veniam, quis nostrud exercitation ullamco laboris nisi ut aliquip ex ea commodo consequat.</p>
    </div>
    <div class="item" style="left:143px;top:63px;width:105px"><span class="dot"><svg><use href="#i-star"/></svg></span><div><span class="ih">Your Text Here</span><p class="tiny">Lorem ipsum dolor sit amet, consectetur adipiscing elit, sed do eiusmod.</p></div></div>
    <div class="item" style="left:143px;top:95px;width:105px"><span class="dot"><svg><use href="#i-chart"/></svg></span><div><span class="ih">Your Text Here</span><p class="tiny">Lorem ipsum dolor sit amet, consectetur adipiscing elit, sed do eiusmod.</p></div></div>
    <div class="item" style="left:143px;top:126px;width:105px"><span class="dot"><svg><use href="#i-gear"/></svg></span><div><span class="ih">Your Text Here</span><p class="tiny">Lorem ipsum dolor sit amet, consectetur adipiscing elit, sed do eiusmod.</p></div></div>
    <div class="item" style="left:143px;top:157px;width:105px"><span class="dot"><svg><use href="#i-search"/></svg></span><div><span class="ih">Your Text Here</span><p class="tiny">Lorem ipsum dolor sit amet, consectetur adipiscing elit, sed do eiusmod.</p></div></div>
    <div class="item" style="left:264px;top:63px;width:105px"><span class="dot"><svg><use href="#i-search"/></svg></span><div><span class="ih">Your Text Here</span><p class="tiny">Lorem ipsum dolor sit amet, consectetur adipiscing elit, sed do eiusmod.</p></div></div>
    <div class="item" style="left:264px;top:95px;width:105px"><span class="dot"><svg><use href="#i-pen"/></svg></span><div><span class="ih">Your Text Here</span><p class="tiny">Lorem ipsum dolor sit amet, consectetur adipiscing elit, sed do eiusmod.</p></div></div>
    <div class="item" style="left:264px;top:126px;width:105px"><span class="dot"><svg><use href="#i-bolt"/></svg></span><div><span class="ih">Your Text Here</span><p class="tiny">Lorem ipsum dolor sit amet, consectetur adipiscing elit, sed do eiusmod.</p></div></div>
    <div class="item" style="left:264px;top:157px;width:105px"><span class="dot"><svg><use href="#i-gear"/></svg></span><div><span class="ih">Your Text Here</span><p class="tiny">Lorem ipsum dolor sit amet, consectetur adipiscing elit, sed do eiusmod.</p></div></div>
    <div class="foot"></div><span class="pg">27</span>
  </section>

  <!-- Row 5 -->
  <section class="slide c1 r5">
    <h2 class="title" style="left:17px;top:20px">Pictures with Bullets</h2>
    <div class="brand" style="left:318px;top:14px">Velsori</div>
    <div class="photo soil" style="left:51px;top:66px;width:66px;height:43px" role="img" aria-label="Hands holding soil"></div>
    <div class="photo snow-grass" style="left:122px;top:66px;width:66px;height:43px" role="img" aria-label="Green shoots in snow"></div>
    <div class="photo sprout" style="left:193px;top:66px;width:66px;height:43px" role="img" aria-label="Hands holding a young seedling"></div>
    <div class="photo soil" style="left:264px;top:66px;width:68px;height:43px" role="img" aria-label="Hands holding soil with a sprout"></div>
    <span class="dot abs" style="left:113px;top:81px"><svg><use href="#i-search"/></svg></span>
    <span class="dot abs" style="left:184px;top:81px"><svg><use href="#i-gear"/></svg></span>
    <span class="dot abs" style="left:255px;top:81px"><svg><use href="#i-chart"/></svg></span>
    <div class="abs" style="left:50px;top:128px;width:135px">
      <span class="head">Heading Goes Here</span>
      <p class="tiny" style="margin-top:2px">Lorem ipsum dolor sit amet, consectetur adipiscing elit, sed do eiusmod tempor incididunt ut labore et commodo consequat dolore magna aliqua.</p>
      <p class="tiny" style="margin-top:5px">Duis aute irure dolor in reprehenderit in voluptate velit esse cillum dolore eu fugiat nulla pariatur.</p>
    </div>
    <div class="abs" style="left:202px;top:128px;width:135px">
      <span class="head">Heading Goes Here</span>
      <p class="tiny" style="margin-top:2px">Lorem ipsum dolor sit amet, consectetur adipiscing elit, sed do eiusmod tempor incididunt ut labore et commodo consequat dolore magna aliqua.</p>
      <p class="tiny" style="margin-top:5px">Duis aute irure dolor in reprehenderit in voluptate velit esse cillum dolore eu fugiat nulla pariatur.</p>
    </div>
    <div class="foot"></div><span class="pg">28</span>
  </section>

  <section class="slide c2 r5 wash-beans" role="img" aria-label="Divider slide over a photo of green beans spilling from a wooden scoop">
    <div class="brand light" style="left:320px;top:18px">Velsori</div>
    <p class="abs" style="left:78px;top:113px;color:#3a3a1a;font-size:5px">Divider Page</p>
    <h2 class="abs" style="left:23px;top:121px;color:#fff;font-size:15px;font-weight:400">Your Title Goes Here</h2>
    <p class="abs" style="left:61px;top:142px;color:#3a3a1a;font-size:7px">Your Subtitle Here</p>
  </section>

  <section class="slide c3 r5">
    <h2 class="title plain" style="left:17px;top:20px">Your Title Goes Here</h2>
    <div class="abs" style="left:17px;top:48px;width:165px">
      <span class="head">Heading Goes Here</span>
      <p class="tiny" style="margin-top:1px">Lorem ipsum dolor sit amet, consectetur adipiscing elit, sed do eiusmod tempor incididunt ut labore et commodo consequat dolore magna aliqua.</p>
      <p class="tiny" style="margin-top:5px">Duis aute irure dolor in reprehenderit in voluptate velit esse cillum dolore eu fugiat nulla pariatur.</p>
    </div>
    <div class="photo lab" style="left:192px;top:5px;width:90px;height:101px" role="img" aria-label="Person in white shirt, torso only"></div>
    <div class="photo lab" style="left:287px;top:5px;width:91px;height:101px" role="img" aria-label="Person in white shirt, torso only"></div>
    <div class="photo sprout" style="left:5px;top:111px;width:182px;height:101px" role="img" aria-label="Open hands holding soil with a seedling"></div>
    <div class="photo soil" style="left:192px;top:111px;width:90px;height:101px" role="img" aria-label="Cupped hands holding soil"></div>
    <div class="photo soil" style="left:287px;top:111px;width:91px;height:101px" role="img" aria-label="Cupped hands holding soil"></div>
  </section>

</main>
</body>
</html>
```